In-Design Template: Single-sided A3 Brochure

Hi In-Design Experts,

I am after an A3 template which is created using In-Design. It needs to be able to operate in CS3.

This template will be used as the basis for a brochure for a beautiful range of stationery. In order to help me with the layout of the brochure, I require a template to be created using "In-Design". The template that you will create will include Rectangle Frames that will allow me to easily insert my products.

As this template is hard to describe in words, I have attached a diagram of what I am actually after. This is an A3 brochure (created on a slightly bigger canvas). As you will see, the right side is an exact replica of the left side. In creating the brochure, think of beautiful shades of pinks - incorporating baby pinks and pastel pinks - elegant, classy and beautiful.

Further details provided below and in the attached files.

If you require any further information or have any questions, please let me know.

Looking forward to seeing your designs.

Target Market(s)

Women

Requirements
Must have
• Template must be created using "In-Design" and be able to operate in version CS3.
• Template information - In the supporting files, I have set out the following:
• - Size of template (Image A3 created on canvas size SRA3 (450 x 320mm) with crop marks
• - Location of all text areas
• - Location of the boxes for my products - Please use the "Rectangle Frame Tool" to allow me to insert products later on.
• Further Design Work - The template is the basis and I would then require your creativity for the following design work:
• - Text to be included at the top of each page - "Dorlina" using Edwarian Script (or similar font style. Please use the pink tones described above.
• - Image - I have attached an image that I would like to include in some way. I am thinking of placing this in the corners of the brochure - but opened to ideas. The image is a picture of scattered leaves. The picture I have attached is in shades of purple, however, I would require the leaves in shades of Pink. I am open to how you use these leaves in the template/brochure. You definitely do not need to use the exact leaves as displayed but something similar would be perfect.

```html
<!DOCTYPE html>
<html lang="en">
<head>
<meta charset="utf-8">
<title>Dorlina Stationery Brochure Template</title>
<link rel="stylesheet" href="https://fonts.googleapis.com/css2?family=Pinyon+Script&family=Jost:wght@400&display=swap">
<style>
  :root {
    --paper: #ffffff;
    --sheet-edge: #f4f4f4;
    --ink: #5b5b5b;
    --ink-soft: #6a6a6a;
    --frame-line: #c4c4c4;
    --crop-line: #3a3a3a;
    --leaf-deep: rgba(214, 120, 148, 0.55);
    --leaf-mid: rgba(232, 164, 183, 0.45);
    --leaf-pale: rgba(245, 205, 215, 0.5);
  }
  * { box-sizing: border-box; margin: 0; padding: 0; }
  html, body {
    width: 1200px; height: 880px; overflow: hidden;
    background: var(--paper);
  }
  .sheet {
    position: relative; width: 1200px; height: 880px;
    background: var(--paper);
    font-family: "Jost", "Futura", sans-serif;
    color: var(--ink);
  }
  .crop-marks { position: absolute; inset: 0; }
  .page {
    position: absolute; top: 36px; height: 808px;
    overflow: hidden; background: var(--paper);
  }
  .page--left { left: 30px; width: 553px; }
  .page--right { left: 612px; width: 558px; }

  .leaf-scatter { position: absolute; inset: 0; pointer-events: none; }
  .page--left .leaf-scatter {
    background:
      radial-gradient(ellipse 260px 110px at 420px 20px, var(--leaf-mid), transparent 70%),
      radial-gradient(ellipse 200px 120px at 180px 60px, var(--leaf-deep), transparent 70%),
      radial-gradient(ellipse 180px 90px at 520px 60px, var(--leaf-pale), transparent 70%),
      radial-gradient(ellipse 70px 200px at 10px 260px, var(--leaf-pale), transparent 70%),
      radial-gradient(ellipse 60px 90px at 15px 660px, var(--leaf-mid), transparent 70%),
      radial-gradient(ellipse 60px 80px at 20px 790px, var(--leaf-deep), transparent 70%);
  }
  .page--right .leaf-scatter {
    background:
      radial-gradient(ellipse 300px 160px at 470px 70px, var(--leaf-deep), transparent 70%),
      radial-gradient(ellipse 220px 90px at 60px 40px, var(--leaf-mid), transparent 70%),
      radial-gradient(ellipse 90px 260px at 545px 280px, var(--leaf-mid), transparent 70%),
      radial-gradient(ellipse 60px 120px at 550px 500px, var(--leaf-pale), transparent 70%),
      radial-gradient(ellipse 90px 80px at 540px 790px, var(--leaf-pale), transparent 70%);
  }

  .page-title {
    position: absolute; top: 18px;
    font-family: "Pinyon Script", "Edwardian Script ITC", cursive;
    font-weight: 400; font-size: 84px; line-height: 1;
    color: var(--ink); letter-spacing: 1px;
  }
  .page--left .page-title { left: 112px; }
  .page--right .page-title { left: 88px; }

  .page-intro, .page-web {
    position: absolute; width: 320px; text-align: center;
    color: var(--ink-soft);
  }
  .page-intro { top: 110px; font-size: 12.5px; }
  .page-web { top: 776px; font-size: 14.5px; letter-spacing: 0.3px; }
  .page--left .page-intro, .page--left .page-web { left: 130px; }
  .page--right .page-intro, .page--right .page-web { left: 108px; }

  .product-grid {
    position: absolute; top: 136px;
    display: grid;
    grid-template-columns: repeat(8, 53px);
    grid-auto-rows: 80.2px;
    column-gap: 13.8px; row-gap: 12px;
    list-style: none;
  }
  .page--left .product-grid { left: 30px; }
  .page--right .product-grid { left: 8px; }
  .product-slot { display: flex; flex-direction: column; align-items: center; }
  .product-frame {
    width: 53px; height: 66px;
    background: var(--paper);
    border: 1px solid var(--frame-line);
  }
  .product-label { margin-top: 2px; font-size: 10px; line-height: 12px; color: var(--ink); }
</style>
</head>
<body>
<main class="sheet">
  <svg class="crop-marks" width="1200" height="880" aria-hidden="true">
    <g stroke="var(--crop-line)" stroke-width="0.8">
      <line x1="0" y1="36" x2="22" y2="36"/><line x1="30" y1="0" x2="30" y2="26"/>
      <line x1="1178" y1="36" x2="1200" y2="36"/><line x1="1170" y1="0" x2="1170" y2="26"/>
      <line x1="0" y1="844" x2="22" y2="844"/><line x1="30" y1="854" x2="30" y2="880"/>
      <line x1="1178" y1="844" x2="1200" y2="844"/><line x1="1170" y1="854" x2="1170" y2="880"/>
    </g>
  </svg>

  <section class="page page--left">
    <div class="leaf-scatter" role="img" aria-label="Scattered pastel pink leaves across the top and left edge"></div>
    <h1 class="page-title">Dorlina</h1>
    <p class="page-intro">Editable text box here for your copy.</p>
    <ul class="product-grid">
      <li class="product-slot"><div class="product-frame"></div><span class="product-label">Text</span></li>
      <li class="product-slot"><div class="product-frame"></div><span class="product-label">Text</span></li>
      <li class="product-slot"><div class="product-frame"></div><span class="product-label">Text</span></li>
      <li class="product-slot"><div class="product-frame"></div><span class="product-label">Text</span></li>
      <li class="product-slot"><div class="product-frame"></div><span class="product-label">Text</span></li>
      <li class="product-slot"><div class="product-frame"></div><span class="product-label">Text</span></li>
      <li class="product-slot"><div class="product-frame"></div><span class="product-label">Text</span></li>
      <li class="product-slot"><div class="product-frame"></div><span class="product-label">Text</span></li>
      <li class="product-slot"><div class="product-frame"></div><span class="product-label">Text</span></li>
      <li class="product-slot"><div class="product-frame"></div><span class="product-label">Text</span></li>
      <li class="product-slot"><div class="product-frame"></div><span class="product-label">Text</span></li>
      <li class="product-slot"><div class="product-frame"></div><span class="product-label">Text</span></li>
      <li class="product-slot"><div class="product-frame"></div><span class="product-label">Text</span></li>
      <li class="product-slot"><div class="product-frame"></div><span class="product-label">Text</span></li>
      <li class="product-slot"><div class="product-frame"></div><span class="product-label">Text</span></li>
      <li class="product-slot"><div class="product-frame"></div><span class="product-label">Text</span></li>
      <li class="product-slot"><div class="product-frame"></div><span class="product-label">Text</span></li>
      <li class="product-slot"><div class="product-frame"></div><span class="product-label">Text</span></li>
      <li class="product-slot"><div class="product-frame"></div><span class="product-label">Text</span></li>
      <li class="product-slot"><div class="product-frame"></div><span class="product-label">Text</span></li>
      <li class="product-slot"><div class="product-frame"></div><span class="product-label">Text</span></li>
      <li class="product-slot"><div class="product-frame"></div><span class="product-label">Text</span></li>
      <li class="product-slot"><div class="product-frame"></div><span class="product-label">Text</span></li>
      <li class="product-slot"><div class="product-frame"></div><span class="product-label">Text</span></li>
      <li class="product-slot"><div class="product-frame"></div><span class="product-label">Text</span></li>
      <li class="product-slot"><div class="product-frame"></div><span class="product-label">Text</span></li>
      <li class="product-slot"><div class="product-frame"></div><span class="product-label">Text</span></li>
      <li class="product-slot"><div class="product-frame"></div><span class="product-label">Text</span></li>
      <li class="product-slot"><div class="product-frame"></div><span class="product-label">Text</span></li>
      <li class="product-slot"><div class="product-frame"></div><span class="product-label">Text</span></li>
      <li class="product-slot"><div class="product-frame"></div><span class="product-label">Text</span></li>
      <li class="product-slot"><div class="product-frame"></div><span class="product-label">Text</span></li>
      <li class="product-slot"><div class="product-frame"></div><span class="product-label">Text</span></li>
      <li class="product-slot"><div class="product-frame"></div><span class="product-label">Text</span></li>
      <li class="product-slot"><div class="product-frame"></div><span class="product-label">Text</span></li>
      <li class="product-slot"><div class="product-frame"></div><span class="product-label">Text</span></li>
      <li class="product-slot"><div class="product-frame"></div><span class="product-label">Text</span></li>
      <li class="product-slot"><div class="product-frame"></div><span class="product-label">Text</span></li>
      <li class="product-slot"><div class="product-frame"></div><span class="product-label">Text</span></li>
      <li class="product-slot"><div class="product-frame"></div><span class="product-label">Text</span></li>
      <li class="product-slot"><div class="product-frame"></div><span class="product-label">Text</span></li>
      <li class="product-slot"><div class="product-frame"></div><span class="product-label">Text</span></li>
      <li class="product-slot"><div class="product-frame"></div><span class="product-label">Text</span></li>
      <li class="product-slot"><div class="product-frame"></div><span class="product-label">Text</span></li>
      <li class="product-slot"><div class="product-frame"></div><span class="product-label">Text</span></li>
      <li class="product-slot"><div class="product-frame"></div><span class="product-label">Text</span></li>
      <li class="product-slot"><div class="product-frame"></div><span class="product-label">Text</span></li>
      <li class="product-slot"><div class="product-frame"></div><span class="product-label">Text</span></li>
      <li class="product-slot"><div class="product-frame"></div><span class="product-label">Text</span></li>
      <li class="product-slot"><div class="product-frame"></div><span class="product-label">Text</span></li>
      <li class="product-slot"><div class="product-frame"></div><span class="product-label">Text</span></li>
      <li class="product-slot"><div class="product-frame"></div><span class="product-label">Text</span></li>
      <li class="product-slot"><div class="product-frame"></div><span class="product-label">Text</span></li>
      <li class="product-slot"><div class="product-frame"></div><span class="product-label">Text</span></li>
      <li class="product-slot"><div class="product-frame"></div><span class="product-label">Text</span></li>
      <li class="product-slot"><div class="product-frame"></div><span class="product-label">Text</span></li>
    </ul>
    <p class="page-web">www.yourwebaddresshere.com</p>
  </section>

  <section class="page page--right">
    <div class="leaf-scatter" role="img" aria-label="Scattered pastel pink leaves across the top and right edge"></div>
    <h2 class="page-title">Dorlina</h2>
    <p class="page-intro">Editable text box here for your copy.</p>
    <ul class="product-grid">
      <li class="product-slot"><div class="product-frame"></div><span class="product-label">Text</span></li>
      <li class="product-slot"><div class="product-frame"></div><span class="product-label">Text</span></li>
      <li class="product-slot"><div class="product-frame"></div><span class="product-label">Text</span></li>
      <li class="product-slot"><div class="product-frame"></div><span class="product-label">Text</span></li>
      <li class="product-slot"><div class="product-frame"></div><span class="product-label">Text</span></li>
      <li class="product-slot"><div class="product-frame"></div><span class="product-label">Text</span></li>
      <li class="product-slot"><div class="product-frame"></div><span class="product-label">Text</span></li>
      <li class="product-slot"><div class="product-frame"></div><span class="product-label">Text</span></li>
      <li class="product-slot"><div class="product-frame"></div><span class="product-label">Text</span></li>
      <li class="product-slot"><div class="product-frame"></div><span class="product-label">Text</span></li>
      <li class="product-slot"><div class="product-frame"></div><span class="product-label">Text</span></li>
      <li class="product-slot"><div class="product-frame"></div><span class="product-label">Text</span></li>
      <li class="product-slot"><div class="product-frame"></div><span class="product-label">Text</span></li>
      <li class="product-slot"><div class="product-frame"></div><span class="product-label">Text</span></li>
      <li class="product-slot"><div class="product-frame"></div><span class="product-label">Text</span></li>
      <li class="product-slot"><div class="product-frame"></div><span class="product-label">Text</span></li>
      <li class="product-slot"><div class="product-frame"></div><span class="product-label">Text</span></li>
      <li class="product-slot"><div class="product-frame"></div><span class="product-label">Text</span></li>
      <li class="product-slot"><div class="product-frame"></div><span class="product-label">Text</span></li>
      <li class="product-slot"><div class="product-frame"></div><span class="product-label">Text</span></li>
      <li class="product-slot"><div class="product-frame"></div><span class="product-label">Text</span></li>
      <li class="product-slot"><div class="product-frame"></div><span class="product-label">Text</span></li>
      <li class="product-slot"><div class="product-frame"></div><span class="product-label">Text</span></li>
      <li class="product-slot"><div class="product-frame"></div><span class="product-label">Text</span></li>
      <li class="product-slot"><div class="product-frame"></div><span class="product-label">Text</span></li>
      <li class="product-slot"><div class="product-frame"></div><span class="product-label">Text</span></li>
      <li class="product-slot"><div class="product-frame"></div><span class="product-label">Text</span></li>
      <li class="product-slot"><div class="product-frame"></div><span class="product-label">Text</span></li>
      <li class="product-slot"><div class="product-frame"></div><span class="product-label">Text</span></li>
      <li class="product-slot"><div class="product-frame"></div><span class="product-label">Text</span></li>
      <li class="product-slot"><div class="product-frame"></div><span class="product-label">Text</span></li>
      <li class="product-slot"><div class="product-frame"></div><span class="product-label">Text</span></li>
      <li class="product-slot"><div class="product-frame"></div><span class="product-label">Text</span></li>
      <li class="product-slot"><div class="product-frame"></div><span class="product-label">Text</span></li>
      <li class="product-slot"><div class="product-frame"></div><span class="product-label">Text</span></li>
      <li class="product-slot"><div class="product-frame"></div><span class="product-label">Text</span></li>
      <li class="product-slot"><div class="product-frame"></div><span class="product-label">Text</span></li>
      <li class="product-slot"><div class="product-frame"></div><span class="product-label">Text</span></li>
      <li class="product-slot"><div class="product-frame"></div><span class="product-label">Text</span></li>
      <li class="product-slot"><div class="product-frame"></div><span class="product-label">Text</span></li>
      <li class="product-slot"><div class="product-frame"></div><span class="product-label">Text</span></li>
      <li class="product-slot"><div class="product-frame"></div><span class="product-label">Text</span></li>
      <li class="product-slot"><div class="product-frame"></div><span class="product-label">Text</span></li>
      <li class="product-slot"><div class="product-frame"></div><span class="product-label">Text</span></li>
      <li class="product-slot"><div class="product-frame"></div><span class="product-label">Text</span></li>
      <li class="product-slot"><div class="product-frame"></div><span class="product-label">Text</span></li>
      <li class="product-slot"><div class="product-frame"></div><span class="product-label">Text</span></li>
      <li class="product-slot"><div class="product-frame"></div><span class="product-label">Text</span></li>
      <li class="product-slot"><div class="product-frame"></div><span class="product-label">Text</span></li>
      <li class="product-slot"><div class="product-frame"></div><span class="product-label">Text</span></li>
      <li class="product-slot"><div class="product-frame"></div><span class="product-label">Text</span></li>
      <li class="product-slot"><div class="product-frame"></div><span class="product-label">Text</span></li>
      <li class="product-slot"><div class="product-frame"></div><span class="product-label">Text</span></li>
      <li class="product-slot"><div class="product-frame"></div><span class="product-label">Text</span></li>
      <li class="product-slot"><div class="product-frame"></div><span class="product-label">Text</span></li>
      <li class="product-slot"><div class="product-frame"></div><span class="product-label">Text</span></li>
    </ul>
    <p class="page-web">www.yourwebaddresshere.com</p>
  </section>
</main>
</body>
</html>
```